Restaurant Menu Design for Meal Prep offered in a food display cooler at a local Gym

I am looking for a menu design with the following items . I would like a workable copy if possible so in the future we can change pricing on this file , or change items . This file will be uploaded on a USB drive and then plugged into a TV. Please ensure a JPEG file is included so this will also work on this TV.

Have a look at our website , www.quilvarkitchen.com for ideas for design that represent the brand appropriately.
The below are the menu items that we would need displayed along with their pricing.

BREAKFAST MEAL PREP ITEMS
Blueberry Pancakes $12.00
Copper Lantern Burrito $10.95

LUNCH/DINNER MEAL PREP OPTIONS
BBQ Glazed Salmon $16.50
Cheeseburger Bowl $13.50
Chicken Alfredo $12.00
Pesto Chicken Pasta $12.00
Chicken Parmesan $13.00
Taco Bowl $14.00
Steak Bite and Green Stir Fry $12.00
Asian Chicken Teriyaki $12.00
Marlowe Stir Fry $15.95

I will attach our logo below, this will need to be on the design. The "heading" (for example breakfast meal prep items and lunch/dinner meal prep options) for the menu should also be on the design.

Ive attached a couple of photos that you need to add to your design.

This will be displayed in a GYM

Meal Prep + Fitness Industry

• Quilvar Logo and Photos attached
• Maybe incorporate something that represents working out or healthy lifestyle in design without going too overboard

```html
<!DOCTYPE html>
<html lang="en">
<head>
<meta charset="utf-8">
<title>Quilvar Meal Prep Menu</title>
<link rel="stylesheet" href="https://fonts.googleapis.com/css2?family=Poppins:wght@700;800&family=Source+Sans+3:wght@400;700&display=swap">
<style>
  :root {
    --backdrop: #d1d3d4;
    --paper: #ffffff;
    --leaf-green: #8dc021;
    --slate-gray: #8a8a8a;
    --dash-gray: #777777;
    --photo-light: #dfe4e6;
    --photo-warm: #e6c9a0;
    --photo-pasta: #8f9a5a;
  }
  * { margin: 0; padding: 0; box-sizing: border-box; }
  html, body { width: 1200px; height: 1200px; overflow: hidden; background: var(--backdrop); }
  .menu-sheet {
    position: absolute; left: 246px; top: 103px; width: 708px; height: 993px;
    background: var(--paper); overflow: hidden;
    font-family: "Source Sans 3", "Myriad Pro", sans-serif;
  }
  .hero-art { position: absolute; left: 0; top: 0; }
  .brand { position: absolute; left: 372px; top: 56px; width: 310px; }
  .brand-name {
    display: flex; align-items: center; gap: 10px;
    font-family: "Poppins", sans-serif; font-weight: 700; font-size: 52px; line-height: 1;
    color: var(--slate-gray); letter-spacing: 1px;
  }
  .brand-dot { width: 18px; height: 18px; border-radius: 50%; background: var(--leaf-green); flex: none; }
  .brand-tagline {
    margin-top: 6px; margin-left: 8px;
    font-family: "Poppins", sans-serif; font-weight: 700; font-size: 17px; color: var(--leaf-green);
    white-space: nowrap;
  }
  .headline {
    position: absolute; left: 0; top: 421px; width: 708px; text-align: center;
    font-family: "Poppins", sans-serif; font-weight: 700; font-size: 28px; line-height: 36px;
  }
  .headline .line-green { color: var(--leaf-green); display: block; }
  .headline .line-gray { color: var(--slate-gray); display: block; }
  .section-title {
    position: absolute; font-weight: 700; font-size: 18px; color: var(--leaf-green); white-space: nowrap;
  }
  .breakfast-title { left: 47px; top: 552px; }
  .lunch-title { left: 347px; top: 516px; }
  .item-box { position: absolute; border: 1px dashed var(--leaf-green); }
  .breakfast-box { left: 47px; top: 580px; width: 266px; height: 87px; }
  .lunch-box { left: 347px; top: 543px; width: 315px; height: 336px; }
  .item-list { list-style: none; }
  .item-list li {
    font-weight: 700; font-size: 18px; color: var(--slate-gray); white-space: nowrap;
    padding-left: 10px; border-bottom: 1px dashed var(--leaf-green); margin-right: 9px; margin-left: 6px;
    padding-left: 4px;
  }
  .item-list li:last-child { border-bottom: none; }
  .breakfast-box li { height: 43px; line-height: 42px; }
  .lunch-box li { height: 35.8px; line-height: 43px; }
  .lunch-box li + li { line-height: 36px; }
  .contact { position: absolute; left: 47px; top: 686px; }
  .contact-title { font-weight: 700; font-size: 25px; color: var(--leaf-green); line-height: 32px; }
  .contact-line { font-size: 15px; color: var(--slate-gray); line-height: 20px; }
  .order-button {
    position: absolute; left: 47px; top: 810px; width: 188px; height: 49px;
    background: var(--leaf-green); border-radius: 25px;
    color: var(--paper); font-weight: 700; font-size: 26px; line-height: 49px; text-align: center;
  }
  .footer-wave { position: absolute; left: 0; top: 0; }
</style>
</head>
<body>
  <main class="menu-sheet">
    <svg class="hero-art" width="708" height="400" viewBox="0 0 708 400">
      <defs>
        <linearGradient id="pancakeTone" x1="0" y1="0" x2="1" y2="1">
          <stop offset="0" stop-color="var(--photo-light)"/>
          <stop offset="0.45" stop-color="var(--photo-warm)"/>
          <stop offset="1" stop-color="var(--photo-light)"/>
        </linearGradient>
        <radialGradient id="pastaTone" cx="0.5" cy="0.55" r="0.6">
          <stop offset="0" stop-color="var(--photo-pasta)"/>
          <stop offset="0.7" stop-color="#c9c4b0"/>
          <stop offset="1" stop-color="var(--photo-light)"/>
        </radialGradient>
      </defs>
      <path role="img" aria-label="Photo of blueberry pancakes stacked on a white plate over a rustic wooden table"
            d="M0,0 L318,0 C352,45 362,110 360,160 L360,300 C300,340 220,362 140,353 C80,345 30,325 0,300 Z"
            fill="url(#pancakeTone)"/>
      <path d="M310,-4 C352,40 370,120 366,206 M340,330 C260,372 170,372 110,362 C60,352 25,335 0,318"
            fill="none" stroke="var(--leaf-green)" stroke-width="2" stroke-dasharray="7 5"/>
      <circle cx="344" cy="270" r="137" fill="var(--paper)"/>
      <circle cx="344" cy="270" r="131" fill="none" stroke="var(--dash-gray)" stroke-width="1.3" stroke-dasharray="4 3"/>
      <circle role="img" aria-label="Photo of pesto chicken penne pasta with broccoli in a white bowl"
              cx="344" cy="270" r="124" fill="url(#pastaTone)"/>
    </svg>

    <div class="brand">
      <div class="brand-name"><span class="brand-dot"></span>QUILVAR</div>
      <div class="brand-tagline">HEALTHY KITCHEN&nbsp;&nbsp;|&nbsp;&nbsp;MEAL PREP</div>
    </div>

    <h1 class="headline">
      <span class="line-green">BREAKFAST MEAL PREP ITEMS AND</span>
      <span class="line-gray">LUNCH/DINNER MEAL PREP OPTIONS</span>
    </h1>

    <h2 class="section-title breakfast-title">BREAKFAST MEAL PREP ITEMS</h2>
    <div class="item-box breakfast-box">
      <ul class="item-list">
        <li>Blueberry Pancakes $12.00</li>
        <li>Copper Lantern Burrito $10.95</li>
      </ul>
    </div>

    <h2 class="section-title lunch-title">LUNCH/DINNER MEAL PREP OPTIONS</h2>
    <div class="item-box lunch-box">
      <ul class="item-list">
        <li>BBQ Glazed Salmon $16.50</li>
        <li>Cheeseburger Bowl $13.50</li>
        <li>Chicken Alfredo $12.00</li>
        <li>Pesto Chicken Pasta $12.00</li>
        <li>Chicken Parmesan $13.00</li>
        <li>Taco Bowl $14.00</li>
        <li>Steak Bite and Green Stir Fry $12.00</li>
        <li>Asian Chicken Teriyaki $12.00</li>
        <li>Marlowe Stir Fry $15.95</li>
      </ul>
    </div>

    <section class="contact">
      <h2 class="contact-title">CONTACT US!</h2>
      <p class="contact-line">++ 123 456 7890</p>
      <p class="contact-line">youremail.com</p>
      <p class="contact-line">www.quilvarkitchen.com</p>
    </section>

    <div class="order-button">ORDER NOW!</div>

    <svg class="footer-wave" width="708" height="993" viewBox="0 0 708 993">
      <path d="M0,900 C150,880 300,912 440,930 C580,948 670,890 708,853 L708,993 L0,993 Z" fill="var(--leaf-green)"/>
    </svg>
  </main>
</body>
</html>
```